Offshore Energy Projects Management Consultancy needs a business card design

Logo available. We provide teams to deliver engineering consultancy, project management and delivery teams mainly in the offshore renewables sector. The company is all about bringing the right people to a project to deliver the scope.

The business card will be used for all staff.

The business card should be quite simple, vibrant and uncluttered but convey experience, enthusiasm and integration.

Target Market(s)

Energy Project Developers and Tier 1 construction companies

Contact Information for Business Card

Logo should be on the back of the card. I'm happy for the designer to play with the colour of the logo and background colour.

Front of the card should convey all the must have information in a clear and professional manner but without being overly traditional.

Colors

Designer to choose colors to be used in the design.

Requirements
Must have
• Land Line Tel Number, Mobile Tel Number, Email, business address, web address.

```html
<!DOCTYPE html>
<html lang="en">
<head>
<meta charset="utf-8">
<title>Tidewater Project Partners – Business Card</title>
<link href="https://fonts.googleapis.com/css2?family=Open+Sans:wght@400;600;700&display=swap" rel="stylesheet">
<style>
  :root {
    --backdrop: #3a3a3c;
    --card: #232325;
    --card-edge: #1b1b1d;
    --blue: #2f6fc0;
    --blue-light: #3d94dc;
    --white: #f2f2f2;
    --grey: #b9b9bb;
    --emboss: #5e5e62;
  }
  * { margin: 0; padding: 0; box-sizing: border-box; }
  html, body { width: 799px; height: 1200px; overflow: hidden; }
  body {
    background: var(--backdrop);
    font-family: "Open Sans", Arial, sans-serif;
    position: relative;
  }
  .card {
    position: absolute;
    left: 80px;
    width: 640px;
    height: 366px;
    background: var(--card);
    border: 1px solid var(--card-edge);
    border-radius: 4px;
    overflow: hidden;
    box-shadow: 0 18px 40px rgba(0,0,0,0.45);
  }
  .card--back { top: 117px; }
  .card--front { top: 717px; }

  /* Back */
  .back-brand {
    position: absolute;
    top: 128px;
    width: 100%;
    text-align: center;
    font-weight: 700;
    font-size: 34px;
    letter-spacing: 1px;
    color: var(--emboss);
    text-transform: uppercase;
    line-height: 1.15;
  }
  .back-web {
    position: absolute;
    top: 248px;
    width: 100%;
    text-align: center;
    font-size: 17px;
    color: var(--white);
  }

  /* Front */
  .waves { position: absolute; inset: 0; }
  .brand {
    position: absolute;
    left: 40px;
    top: 118px;
    display: flex;
    align-items: center;
    gap: 12px;
  }
  .brand-dot {
    width: 20px; height: 20px;
    border-radius: 50%;
    background: var(--blue);
    flex: none;
  }
  .brand-name {
    font-weight: 700;
    font-size: 26px;
    line-height: 1.15;
    color: var(--white);
    text-transform: uppercase;
    letter-spacing: 0.5px;
  }
  .person {
    position: absolute;
    right: 44px;
    top: 92px;
    text-align: right;
    color: var(--white);
  }
  .person-name { font-weight: 600; font-size: 25px; }
  .person-role { font-size: 15px; }
  .address {
    position: absolute;
    left: 40px;
    top: 232px;
    font-size: 14px;
    line-height: 1.4;
    color: var(--white);
  }
  .contacts {
    position: absolute;
    right: 36px;
    bottom: 26px;
    list-style: none;
    font-size: 15px;
    color: var(--white);
  }
  .contacts li {
    display: flex;
    justify-content: flex-end;
    align-items: center;
    gap: 12px;
    line-height: 1.5;
  }
  .contacts svg { width: 15px; height: 15px; fill: var(--blue-light); flex: none; }
</style>
</head>
<body>

  <section class="card card--back">
    <div class="back-brand">Tidewater<br>Project Partners</div>
    <div class="back-web">www.tidewaterpartners.com</div>
  </section>

  <section class="card card--front">
    <svg class="waves" viewBox="0 0 640 366" preserveAspectRatio="none">
      <path d="M0,0 H640 V250 C560,232 470,200 420,130 C370,62 250,18 0,16 Z" fill="var(--blue)"/>
      <path d="M0,0 H640 V40 C560,30 470,20 400,10 C300,0 150,0 0,6 Z" fill="var(--blue-light)" opacity="0.7"/>
      <path d="M120,30 C250,34 340,70 380,120" fill="none" stroke="var(--card)" stroke-width="4"/>
      <path d="M0,24 C250,28 360,72 410,142 C460,212 560,246 640,262 V272 C550,258 450,228 398,152 C348,82 250,36 0,32 Z" fill="var(--blue-light)"/>
    </svg>

    <div class="brand">
      <span class="brand-dot"></span>
      <div class="brand-name">Tidewater<br>Project Partners</div>
    </div>

    <div class="person">
      <div class="person-name">Daniel Marsh</div>
      <div class="person-role">Managing Director</div>
    </div>

    <div class="address">18 Harbour Quay, Port Ellis,<br>Northgate, US 204810</div>

    <ul class="contacts">
      <li>024 518 7730
        <svg viewBox="0 0 24 24"><path d="M6.6 10.8a15.1 15.1 0 0 0 6.6 6.6l2.2-2.2c.3-.3.7-.4 1-.2 1.1.4 2.3.6 3.6.6.6 0 1 .4 1 1V20c0 .6-.4 1-1 1A17 17 0 0 1 3 4c0-.6.4-1 1-1h3.5c.6 0 1 .4 1 1 0 1.3.2 2.5.6 3.6.1.3 0 .7-.2 1z"/></svg>
      </li>
      <li>037 642 9185
        <svg viewBox="0 0 24 24"><path d="M6.6 10.8a15.1 15.1 0 0 0 6.6 6.6l2.2-2.2c.3-.3.7-.4 1-.2 1.1.4 2.3.6 3.6.6.6 0 1 .4 1 1V20c0 .6-.4 1-1 1A17 17 0 0 1 3 4c0-.6.4-1 1-1h3.5c.6 0 1 .4 1 1 0 1.3.2 2.5.6 3.6.1.3 0 .7-.2 1z"/></svg>
      </li>
      <li>daniel@tidewaterpartners.com
        <svg viewBox="0 0 24 24"><path d="M2 5h20v14H2z M2 5l10 8 10-8" fill="none" stroke="var(--blue-light)" stroke-width="2"/><path d="M2 5h20L12 13z"/></svg>
      </li>
      <li>www.tidewaterpartners.com
        <svg viewBox="0 0 24 24"><circle cx="12" cy="12" r="10"/><path d="M2 12h20M12 2c3 3 3 17 0 20M12 2c-3 3-3 17 0 20" fill="none" stroke="var(--card)" stroke-width="1.5"/></svg>
      </li>
    </ul>
  </section>

</body>
</html>
```